Sunvale Ride Co Splashpage

This webpage will be a holding page until our website is complete. This page needs to be designed to advertise our tours in Honolulu, Hawaii. So it is important to have prices displayed and have a Hawaiian theme.

1. Warm colors - suggest reds?
2. Hawaiian flower incorporated in design

3. Display prices
Adult - single Journey - $20
Adult - 1 Day - $20 (this needs to be displayed as a special deal/price because full price is $25)
Adult - 2 days - $30

Seniors - (62+) 1 Day + 1 Day Free - $20

Children 5 - 17 yrs - 1 Day - $13
Children 5 - 17 yrs - 2 Days - $15
Under 5 Yrs - Free

There will be an online booking button (text on button should say "Book Online", so please make sure it is clear where they can purchase the tickets.

3. A photo of our branded double decker bus should be incorporate on the page.

4. Our Message "Welcome to Sunvale Ride Co. Our Open Top Bus ensures you have an unrivalled view of Honolulu and all that this great city has to offer. We pass all of the city’s main sites, offering fantastic photo opportunities along the way. Our tour takes around 90 minutes. You can get on and off the bus as often as you want. Your ticket is valid for one or two days. All departures have commentary in English. If it’s raining, we have a sliding roof to keep you dry. Step on-board and let us show you the best of Honolulu."

5. Some tour sites our tour visits are: Marlow's Arcade, Waikiki beach, Umerik Palace, Bretoma Palace/King statue, Darvin's statue

We are catering to an international adult audience (ranging from 25 - 60 yrs of age) that handles vacation planning.

Please visit www.ridebyloop.ee to get an idea of our style.

• 1. prices displayed where they be viewed easily - There will be an online booking button so please make sure it is clear where they can purchase the tickets.

2. Adult - 1 Day - $20 (this needs to be displayed as a special deal/price because full price is $25)

3. Photo of our double decker bus

4. Hawaiian flower incorporated in design

5. Bright colors (make sure orange isn't the main background color) but not overwhelming

6. Logo on webpage
• 1. Images of our tour sites
2. Other Hawaiian images such as palm trees, Maile Lei, Sun with sunglasses, flower lei, parrot, Hawaiian sunsets
• -Do not want any shade of orange as the main background color

```html
<!DOCTYPE html>
<html lang="en">
<head>
<meta charset="utf-8">
<title>Sunvale Ride Co</title>
<link rel="stylesheet" href="https://fonts.googleapis.com/css2?family=Fredoka:wght@400;500;600;700&family=Lato:wght@400;700&family=Caveat:wght@400;500&display=swap">
<style>
  :root {
    --page-bg: #f6f3ec;
    --panel: #f7efcf;
    --panel-hero: #f3e6b9;
    --tab-active: #5e9e36;
    --tab: #b9dc8f;
    --green-btn: #9fd271;
    --green-ring: #ecdca0;
    --teal: #6fcfd0;
    --red: #b30000;
    --special: #d00000;
    --ink: #2b2217;
    --box: #efe6d1;
    --box-edge: #d9ccae;
  }
  * { box-sizing: border-box; margin: 0; padding: 0; }
  html, body { width: 1126px; height: 1200px; overflow: hidden; background: var(--page-bg); }
  body { position: relative; font-family: "Lato", sans-serif; color: var(--ink); }

  .logo { position: absolute; left: 138px; top: 34px; font-family: "Fredoka", sans-serif; font-weight: 700; font-size: 40px; color: var(--red); letter-spacing: 1px; display: flex; align-items: center; gap: 12px; }
  .logo-dot { width: 22px; height: 22px; border-radius: 50%; background: #f2d82a; }

  .nav { position: absolute; top: 100px; left: 0; width: 100%; height: 46px; }
  .nav-tab { position: absolute; top: 0; height: 48px; border-radius: 5px 5px 0 0; background: var(--tab); color: #fff; font-family: "Fredoka", sans-serif; font-weight: 600; font-size: 19px; display: flex; align-items: center; justify-content: center; text-shadow: 0 1px 1px rgba(0,0,0,.15); }
  .nav-tab.is-active { background: var(--tab-active); transform: rotate(1.5deg); }
  .nav-tab:nth-child(2) { transform: rotate(-.5deg); }
  .nav-tab:nth-child(3) { transform: rotate(-2deg); }
  .nav-tab:nth-child(4) { transform: rotate(3deg); }

  .tropical { position: absolute; }
  .tropical-left { left: 18px; top: 340px; width: 220px; height: 220px; background: radial-gradient(ellipse 45% 40% at 58% 38%, rgba(252,250,238,.95) 0%, rgba(245,240,215,.8) 45%, rgba(150,205,85,.85) 70%, rgba(120,185,55,0) 100%); border-radius: 60% 40% 50% 50%; }
  .tropical-right { left: 912px; top: 340px; width: 210px; height: 230px; background: radial-gradient(ellipse 45% 40% at 42% 38%, rgba(252,250,238,.95) 0%, rgba(245,240,215,.8) 45%, rgba(150,205,85,.85) 70%, rgba(120,185,55,0) 100%); border-radius: 40% 60% 50% 50%; }

  .panel { position: absolute; left: 140px; top: 146px; width: 866px; height: 842px; background: var(--panel); box-shadow: 0 0 4px rgba(120,100,60,.35); }
  .hero-band { position: absolute; left: 136px; top: 146px; width: 870px; height: 309px; background: radial-gradient(ellipse at 30% 40%, #faf3d6, var(--panel-hero)); box-shadow: 0 2px 5px rgba(120,100,60,.35); }

  .hero-arrow { position: absolute; top: 263px; width: 68px; height: 68px; border-radius: 50%; background: var(--green-ring); display: flex; align-items: center; justify-content: center; }
  .hero-arrow span { width: 56px; height: 56px; border-radius: 50%; background: var(--green-btn); display: flex; align-items: center; justify-content: center; }
  .hero-arrow.prev { left: 103px; }
  .hero-arrow.next { left: 964px; }

  .welcome { position: absolute; left: 183px; top: 188px; font-family: "Fredoka", sans-serif; font-weight: 600; font-size: 31px; line-height: 38px; color: var(--teal); }
  .welcome-text { position: absolute; left: 187px; top: 272px; width: 290px; font-size: 14.5px; line-height: 19px; }
  .book-btn { position: absolute; left: 205px; top: 353px; width: 218px; height: 61px; border-radius: 31px; background: var(--green-ring); padding: 5px; }
  .book-btn span { display: flex; width: 100%; height: 100%; border-radius: 26px; background: var(--green-btn); color: #f5f7ea; align-items: center; justify-content: center; font-family: "Fredoka", sans-serif; font-weight: 600; font-size: 26px; letter-spacing: 1px; text-shadow: 0 1px 2px rgba(0,0,0,.25); }

  .bus-photo { position: absolute; left: 491px; top: 176px; width: 463px; height: 252px; border: 5px solid #e7db8a; background: linear-gradient(160deg, #dfe9ef 0%, #c8302c 40%, #b8201c 62%, #6f9c45 85%, #8a8a80 100%); }

  .about-title { position: absolute; left: 183px; top: 514px; font-family: "Fredoka", sans-serif; font-weight: 600; font-size: 26px; color: var(--red); }
  .about-text { position: absolute; left: 183px; top: 555px; width: 385px; font-size: 12.5px; line-height: 23px; }

  .ribbon { position: absolute; height: 44px; background: var(--teal); color: #fff; font-family: "Fredoka", sans-serif; font-size: 29px; display: flex; align-items: center; justify-content: center; border-radius: 3px 3px 0 0; }
  .ribbon-note { position: absolute; font-family: "Caveat", cursive; font-size: 21px; color: var(--ink); white-space: nowrap; }
  .tickets-ribbon { left: 626px; top: 483px; width: 172px; transform: rotate(1.5deg); }
  .tickets-note { left: 804px; top: 496px; }

  .ticket-box { position: absolute; left: 605px; top: 528px; width: 348px; height: 173px; background: var(--box); border: 1px solid var(--box-edge); border-radius: 8px; box-shadow: inset 0 0 6px rgba(150,130,90,.25), 0 2px 3px rgba(120,100,60,.3); padding: 16px 0 0 34px; font-size: 12px; line-height: 15.5px; }
  .price-group { padding-bottom: 7px; margin-bottom: 9px; border-bottom: 2px solid #e2d8c0; width: 222px; white-space: nowrap; }
  .price-group:last-child { border: 0; margin-bottom: 0; }
  .price-special { color: var(--special); }

  .divider { position: absolute; left: 172px; top: 728px; width: 797px; border-top: 1px dashed #8a7d66; }

  .sites-title { position: absolute; left: 181px; top: 757px; font-family: "Fredoka", sans-serif; font-weight: 600; font-size: 26px; line-height: 27px; color: var(--red); }
  .sites-list { position: absolute; left: 181px; top: 820px; width: 240px; list-style: none; font-family: "Caveat", cursive; font-size: 23px; line-height: 23px; white-space: nowrap; }

  .gallery-ribbon { left: 461px; top: 747px; width: 174px; transform: rotate(-2deg); }
  .gallery-note { left: 642px; top: 759px; }
  .gallery-arrow { position: absolute; top: 843px; width: 44px; height: 54px; border-radius: 27px; background: var(--green-btn); }
  .gallery-arrow.prev { left: 424px; }
  .gallery-arrow.next { left: 932px; }
  .gallery-box { position: absolute; left: 446px; top: 792px; width: 508px; height: 140px; background: var(--box); border: 1px solid var(--box-edge); border-radius: 8px; box-shadow: 0 2px 3px rgba(120,100,60,.3); }
  .thumb { position: absolute; top: 29px; width: 81px; height: 81px; border: 4px solid #ede3a4; }
  .thumb-1 { left: 12px; background: linear-gradient(#cfe0f0, #b77a6a 60%, #7d6a58); }
  .thumb-2 { left: 111px; background: linear-gradient(#5fa6e3, #dbe7ef 45%, #3d8fc2 65%, #e0d3a6); }
  .thumb-3 { left: 210px; background: linear-gradient(#a9cbe6, #7d7463 55%, #5f7a3e); }
  .thumb-4 { left: 310px; background: linear-gradient(#4fa3e6, #c79a5a 55%, #4aa0b8); }
  .thumb-5 { left: 409px; background: linear-gradient(#b0c7d6, #8a6a3e 50%, #6f7a3a); }

  .footer-band { position: absolute; left: 140px; top: 950px; width: 866px; height: 38px; background: linear-gradient(rgba(255,255,255,0), rgba(225,235,220,.5)); }
</style>
</head>
<body>
  <div class="logo"><span>Sunvale Ride Co</span><span class="logo-dot"></span></div>

  <nav class="nav">
    <div class="nav-tab is-active" style="left:415px;width:143px">About Us</div>
    <div class="nav-tab" style="left:561px;width:140px">The Tour</div>
    <div class="nav-tab" style="left:706px;width:141px">Buy Online</div>
    <div class="nav-tab" style="left:856px;width:143px">Contact</div>
  </nav>

  <div class="tropical tropical-left" role="img" aria-label="Palm fronds with white plumeria flowers"></div>
  <div class="tropical tropical-right" role="img" aria-label="Palm fronds with white plumeria flowers"></div>
  <div class="panel"></div>
  <div class="hero-band"></div>

  <div class="hero-arrow prev"><span><svg width="22" height="28" viewBox="0 0 22 28"><path d="M16 3 L5 14 L16 25" fill="none" stroke="#fff" stroke-width="6" stroke-linecap="round" stroke-linejoin="round"/></svg></span></div>
  <div class="hero-arrow next"><span><svg width="22" height="28" viewBox="0 0 22 28"><path d="M6 3 L17 14 L6 25" fill="none" stroke="#fff" stroke-width="5" stroke-linecap="round" stroke-linejoin="round"/></svg></span></div>

  <h1 class="welcome">Welcome to<br>Sunvale Ride Co</h1>
  <p class="welcome-text">Our Open Top Bus ensures you have an unrivalled view of Honolulu and all that this great city has to offer</p>
  <div class="book-btn"><span>Book Online</span></div>
  <div class="bus-photo" role="img" aria-label="Photo of the red branded open top double decker tour bus on a city street"></div>

  <h2 class="about-title">About Us</h2>
  <p class="about-text">We pass all of the city’s main sites, offering fantastic photo opportunities along the way. Our tour takes around 90 minutes. You can get on and off the bus as often as you want. Your ticket is valid for one or two days. All departures have commentary in English. If it’s raining, we have a sliding roof to keep you dry. Step on-board and let us show you the best of Honolulu.</p>

  <div class="ribbon tickets-ribbon">Ticket Prices</div>
  <div class="ribbon-note tickets-note">Purchase Online</div>
  <div class="ticket-box">
    <div class="price-group">
      <div>Adult - single Journey - $20</div>
      <div class="price-special">Adult - 1 Day - $20 SPECIAL - Full price is $25</div>
      <div>Adult - 2 days - $30</div>
    </div>
    <div class="price-group">
      <div>Seniors - (62+) 1 Day + 1 Day Free - $20</div>
    </div>
    <div class="price-group">
      <div>Children 5 - 17 yrs - 1 Day - $13</div>
      <div>Children 5 - 17 yrs - 2 Days - $15</div>
      <div>Under 5 Yrs - Free</div>
    </div>
  </div>

  <div class="divider"></div>

  <h2 class="sites-title">Some tour sites<br>our tour visits are:</h2>
  <ul class="sites-list">
    <li>Marlow's Arcade</li>
    <li>Waikiki Beach</li>
    <li>Umerik Palace</li>
    <li>Bretoma Palace/King statue</li>
    <li>Darvin's statue</li>
  </ul>

  <div class="ribbon gallery-ribbon">Tour Gallery</div>
  <div class="ribbon-note gallery-note">Click to Enlarge</div>
  <div class="gallery-arrow prev"></div>
  <div class="gallery-arrow next"></div>
  <div class="gallery-box">
    <div class="thumb thumb-1" role="img" aria-label="Photo of an arcade of shops"></div>
    <div class="thumb thumb-2" role="img" aria-label="Photo of Waikiki Beach and hotels"></div>
    <div class="thumb thumb-3" role="img" aria-label="Photo of a historic palace"></div>
    <div class="thumb thumb-4" role="img" aria-label="Photo of a statue on the beach"></div>
    <div class="thumb thumb-5" role="img" aria-label="Photo of a bronze statue with a guitar"></div>
  </div>

  <div class="footer-band"></div>
</body>
</html>
```